Open House 2017

We need a flyer for an insert for a newspaper for an open house that we are going to have and we are also wanting to list the front of the flyer the 3 pictures of our real estate agents and our Logo.

For the real estate agents : The one with Purple shirt would be the middle picture.

Attached also is our current Logo, Please re-design our Logo a bit to make it look better.

Target Market(s)

Residential and commercial and Land In our rural areas.

Industry/Entity Type

House

Requirements
Must have
• Front page -
• Our logo at the top our 3 pictures at the top after our logo and business address.
• Middle of page Some thing worded similar to the following:"let us place a SOLD sign in your front yard". Or
• " Sold vs. For Sale which would you like to see in your front yard?"
• Our colors for our agency are Gold and Black (the whole flyer does not need to be this color though)
• Join us for an open house in our office
• Wednesday March 1
• 3-6pm
• Back page of flyer: "If you would like to add your name to the Sold Properties list, give us a call today!
• Sold listings which we will get sent to you will also be listed on the back page.
Should not have
• do not make the flyer too "busy" with too many pictures and wording.

```html
<!DOCTYPE html>
<html lang="en">
<head>
<meta charset="utf-8">
<title>Open House Flyer – Harlow Crest Realty LLC</title>
<link rel="stylesheet" href="https://fonts.googleapis.com/css2?family=Roboto+Condensed:wght@700&family=Tinos:wght@400;700&family=Montserrat:wght@500&family=Archivo+Black&family=Lato:wght@400&display=swap">
<style>
  :root {
    --gold: #d9b32b;
    --gold-light: #f3d65a;
    --gold-dark: #a9830f;
    --black: #111111;
    --white: #ffffff;
    --ink: #151515;
    --meadow: #cfe0b5;
    --photo-grey: #8a8a8a;
  }
  html, body {
    margin: 0;
    padding: 0;
    width: 1200px;
    height: 1200px;
    overflow: hidden;
    background: var(--white);
  }
  .flyer {
    position: absolute;
    left: 207px;
    top: 76px;
    width: 821px;
    height: 1055px;
    background: var(--white);
    overflow: hidden;
    box-shadow: 2px 3px 6px rgba(0,0,0,0.35);
  }
  .meadow {
    position: absolute;
    left: 0; top: 684px;
    width: 821px; height: 324px;
    background: linear-gradient(to bottom, rgba(255,255,255,1) 0%, #eef3e6 35%, #d7e5c3 70%, var(--meadow) 100%);
  }
  .header-wave { position: absolute; left: 0; top: 0; }
  .brand-name {
    position: absolute;
    left: 0; width: 821px;
    top: 36px;
    text-align: center;
    font-family: "Tinos", serif;
    font-weight: 400;
    font-size: 40px;
    color: var(--gold);
    letter-spacing: 0.5px;
  }
  .brand-tagline {
    position: absolute;
    right: 226px;
    top: 98px;
    font-family: "Lato", sans-serif;
    font-size: 13px;
    color: var(--gold);
  }
  .agents { position: absolute; left: 0; top: 0; }
  .headline {
    position: absolute;
    left: 0; width: 821px;
    top: 574px;
    text-align: center;
    margin: 0;
  }
  .headline-top {
    display: block;
    font-family: "Roboto Condensed", sans-serif;
    font-weight: 700;
    font-size: 51px;
    line-height: 56px;
    color: var(--gold);
    text-transform: uppercase;
  }
  .headline-bottom {
    display: block;
    font-family: "Tinos", serif;
    font-weight: 700;
    font-size: 31px;
    line-height: 40px;
    color: var(--ink);
    text-transform: uppercase;
  }
  .event-badge { position: absolute; left: 0; top: 0; }
  .event-text {
    position: absolute;
    left: 0; width: 821px;
    text-align: center;
    margin: 0;
  }
  .event-invite {
    top: 717px;
    font-family: "Roboto Condensed", sans-serif;
    font-weight: 700;
    font-size: 34px;
    color: var(--gold);
  }
  .event-place {
    top: 756px;
    font-family: "Montserrat", sans-serif;
    font-weight: 500;
    font-size: 48px;
    color: var(--white);
  }
  .event-date {
    top: 828px;
    font-family: "Roboto Condensed", sans-serif;
    font-weight: 700;
    font-size: 47px;
    color: var(--white);
    text-shadow: 1px 2px 2px rgba(0,0,0,0.35);
  }
  .event-time {
    top: 892px;
    font-family: "Archivo Black", sans-serif;
    font-size: 50px;
    color: var(--white);
  }
  .footer-bar {
    position: absolute;
    left: 0; top: 1008px;
    width: 821px; height: 47px;
    background: var(--black);
    color: var(--white);
    font-family: "Lato", sans-serif;
    font-size: 14px;
    letter-spacing: 8px;
    line-height: 47px;
    text-align: center;
  }
</style>
</head>
<body>
<main class="flyer">
  <div class="meadow" role="img" aria-label="Soft faded photo of a green lawn in front of a country house"></div>

  <svg class="header-wave" width="821" height="220" viewBox="0 0 821 220" aria-hidden="true">
    <defs>
      <linearGradient id="goldSweep" x1="0" x2="1" y1="0" y2="0">
        <stop offset="0" stop-color="var(--gold-dark)"/>
        <stop offset="0.5" stop-color="var(--gold-light)"/>
        <stop offset="1" stop-color="var(--gold-dark)"/>
      </linearGradient>
    </defs>
    <path d="M0 0 H821 V125 C680 140 560 208 415 208 C260 208 140 92 0 92 Z" fill="url(#goldSweep)"/>
    <path d="M0 0 H821 V106 C680 118 560 190 415 190 C260 190 140 78 0 76 Z" fill="var(--white)"/>
    <path d="M0 0 H821 V98 C680 110 560 180 415 180 C260 180 140 70 0 68 Z" fill="var(--black)"/>
  </svg>
  <div class="brand-name">Harlow Crest Realty LLC</div>
  <div class="brand-tagline">“Where the phone is ALWAYS on.”</div>

  <svg class="agents" width="821" height="620" viewBox="0 0 821 620">
    <defs>
      <radialGradient id="portraitTone" cx="0.5" cy="0.45" r="0.6">
        <stop offset="0" stop-color="#a3a3a3"/>
        <stop offset="1" stop-color="var(--photo-grey)"/>
      </radialGradient>
      <linearGradient id="ringGold" x1="0" x2="1" y1="0" y2="1">
        <stop offset="0" stop-color="var(--gold-light)"/>
        <stop offset="0.5" stop-color="var(--gold)"/>
        <stop offset="1" stop-color="var(--gold-dark)"/>
      </linearGradient>
    </defs>
    <ellipse cx="146" cy="518" rx="100" ry="8" fill="rgba(0,0,0,0.12)"/>
    <ellipse cx="675" cy="518" rx="100" ry="8" fill="rgba(0,0,0,0.12)"/>
    <ellipse cx="413" cy="566" rx="140" ry="9" fill="rgba(0,0,0,0.12)"/>

    <circle cx="146" cy="392" r="120" fill="url(#ringGold)"/>
    <circle cx="146" cy="392" r="113" fill="var(--white)"/>
    <circle cx="146" cy="392" r="106" fill="url(#portraitTone)" role="img" aria-label="Portrait photo of an agent in a purple shirt"/>

    <circle cx="675" cy="392" r="120" fill="url(#ringGold)"/>
    <circle cx="675" cy="392" r="113" fill="var(--white)"/>
    <circle cx="675" cy="392" r="106" fill="url(#portraitTone)" role="img" aria-label="Portrait photo of an agent in a checked shirt"/>

    <circle cx="413" cy="390" r="170" fill="url(#ringGold)"/>
    <circle cx="413" cy="390" r="162" fill="var(--white)"/>
    <circle cx="413" cy="390" r="155" fill="url(#portraitTone)" role="img" aria-label="Portrait photo of an agent in a white blouse"/>
  </svg>

  <h1 class="headline">
    <span class="headline-top">Sold vs. For Sale Which Would</span>
    <span class="headline-bottom">You like to see in your front yard?</span>
  </h1>

  <svg class="event-badge" width="821" height="1008" viewBox="0 0 821 1008" aria-hidden="true">
    <defs>
      <linearGradient id="badgeGold" x1="0" x2="1" y1="0" y2="1">
        <stop offset="0" stop-color="var(--gold-light)"/>
        <stop offset="0.5" stop-color="var(--gold)"/>
        <stop offset="1" stop-color="var(--gold-dark)"/>
      </linearGradient>
      <linearGradient id="badgeBlack" x1="0" x2="1" y1="0" y2="0">
        <stop offset="0" stop-color="#000"/>
        <stop offset="0.5" stop-color="#2a2a2a"/>
        <stop offset="1" stop-color="#000"/>
      </linearGradient>
      <linearGradient id="ribbonGold" x1="0" x2="0" y1="0" y2="1">
        <stop offset="0" stop-color="var(--gold)"/>
        <stop offset="0.5" stop-color="var(--gold-light)"/>
        <stop offset="1" stop-color="var(--gold-dark)"/>
      </linearGradient>
    </defs>
    <path d="M148 688 H674 Q704 688 701 718 L683 956 Q681 984 653 984 H169 Q141 984 139 956 L121 718 Q118 688 148 688 Z" fill="url(#badgeGold)"/>
    <path d="M154 700 H668 Q690 700 688 722 L671 952 Q669 972 649 972 H173 Q153 972 151 952 L134 722 Q132 700 154 700 Z" fill="url(#badgeBlack)"/>
    <path d="M113 888 L141 904 L141 888 Z" fill="var(--gold-dark)"/>
    <path d="M705 888 L681 904 L681 888 Z" fill="var(--gold-dark)"/>
    <rect x="113" y="828" width="592" height="60" fill="url(#ribbonGold)"/>
  </svg>
  <p class="event-text event-invite">Join us for an open house</p>
  <p class="event-text event-place">in our office</p>
  <p class="event-text event-date">1st March Wednesday</p>
  <p class="event-text event-time">3 to 6PM</p>

  <footer class="footer-bar">www.harlowcrestrealty.com</footer>
</main>
</body>
</html>
```